Larchmere Hockey Academy

We are are Ice Hockey Development Company that provided on-ice Hockey development services. We need a Landing Page with tabs to direct to individual program pages.
Landing Page
About Page
Winter Program Page
Spring Program Page
Summer Program Page
Team Page
Tournament Page

```html
<!DOCTYPE html>
<html lang="en">
<head>
<meta charset="utf-8">
<title>Larchmere Hockey Academy</title>
<link rel="stylesheet" href="https://fonts.googleapis.com/css2?family=Anton&family=Poppins:wght@400;500;600;700&display=swap">
<style>
:root{
  --green:#1f8f1f;
  --green-dark:#0e6a14;
  --ink:#1b1b1b;
  --text:#4a4a4a;
  --muted:#777;
  --light:#f1f2f3;
  --footer:#2a2a2a;
  --white:#fff;
  --dot:#9fd19f;
}
*{margin:0;padding:0;box-sizing:border-box}
html,body{width:1200px;height:4380px;overflow:hidden;background:var(--white)}
body{position:relative;font-family:"Poppins",sans-serif;color:var(--ink)}
.abs{position:absolute}
.display{font-family:"Anton",sans-serif;text-transform:uppercase;letter-spacing:-.2px;line-height:1;color:var(--ink)}
.photo{position:absolute}
.btn{position:absolute;display:flex;align-items:center;padding-left:26px;background:var(--green);color:var(--white);border-radius:20px;font-size:13px;font-weight:600}

/* header */
.site-header{position:absolute;left:0;top:0;width:1200px;height:83px;background:var(--white)}
.brand{position:absolute;left:160px;top:22px;display:flex;align-items:center;gap:8px;font-family:"Poppins",sans-serif;font-weight:700;font-size:17px;color:var(--ink);line-height:1.05;text-transform:uppercase}
.brand-square{width:14px;height:14px;background:var(--green)}
.nav a{position:absolute;top:35px;font-size:13.5px;font-weight:500;color:var(--ink);text-decoration:none}

/* hero */
.hero-title{position:absolute;left:143px;color:var(--white);font-size:54px}
.hero-copy{position:absolute;left:145px;top:422px;width:500px;color:var(--white);font-size:11.5px;font-weight:500;line-height:2.1}
.slider-dot{position:absolute;left:72px;width:6px;height:6px;border-radius:50%;background:var(--white)}

/* labels */
.side-label{position:absolute;writing-mode:vertical-rl;transform:rotate(180deg);font-size:10px;font-weight:600;text-transform:uppercase;color:var(--ink);padding-bottom:0}
.side-label::after{content:"";display:block;width:1px;height:38px;background:var(--green);margin:8px auto 0}
.side-label.green{color:var(--green)}

.body-copy{position:absolute;font-size:12px;line-height:21px;color:var(--text)}

/* programs */
.dots{position:absolute;background-image:radial-gradient(circle,var(--dot) 1.4px,transparent 1.6px);background-size:12px 12px}
.prog-num{position:absolute;width:50px;height:50px;border:1.5px solid var(--ink);border-radius:50%;display:flex;align-items:center;justify-content:center;font-size:20px;font-weight:600}
.prog-num-label{position:absolute;font-size:9px;color:var(--text)}
.prog-title{position:absolute;font-size:22px;font-weight:500;color:var(--ink)}
.prog-desc{position:absolute;width:350px;font-size:11.5px;line-height:21px;color:var(--text)}

/* tournament */
.t-card{position:absolute;top:2872px;width:237px;height:278px;padding:26px 28px}
.t-card.solid{background:var(--green);color:var(--white)}
.t-card.outline{background:var(--white);border:2px solid #cfd3d6;color:var(--ink)}
.t-card h3{font-family:"Anton",sans-serif;font-weight:400;font-size:20px;line-height:1.25;text-transform:uppercase}
.t-card h4{font-family:"Anton",sans-serif;font-weight:400;font-size:14px;text-transform:uppercase;margin-top:2px}
.t-card .date{display:inline-block;margin-top:12px;padding:2px 12px;border-radius:10px;font-size:9px;font-weight:600;background:var(--white);color:var(--green)}
.t-card.outline .date{background:var(--green);color:var(--white)}
.t-card .place{margin-top:14px;font-size:9px;font-weight:700}
.t-card p{margin-top:12px;font-size:11.5px;line-height:21px}
.t-card .card-btn{position:absolute;left:20px;bottom:-2px;width:150px;height:36px;border-radius:18px;display:flex;align-items:center;padding-left:22px;font-size:13px;font-weight:600}
.t-card.solid .card-btn{background:var(--green-dark);color:var(--white)}
.t-card.outline .card-btn{background:var(--green);color:var(--white)}

/* team */
.coach-name{position:absolute;top:3685px;height:40px;background:var(--white);display:flex;align-items:center;justify-content:center;font-family:"Anton",sans-serif;font-size:17px;text-transform:uppercase;color:var(--ink)}

/* newsletter */
.news-input{position:absolute;left:141px;top:3960px;width:372px;height:46px;border:1.5px solid #9ea3a6;background:var(--white);display:flex;align-items:center;padding-left:44px;font-size:11px;color:#9a9a9a}
.news-btn{position:absolute;left:386px;top:3965px;width:120px;height:36px;background:var(--green);color:var(--white);font-size:10px;font-weight:700;display:flex;align-items:center;padding-left:16px;text-transform:uppercase}

/* footer */
.site-footer{position:absolute;left:0;top:4070px;width:1200px;height:310px;background:var(--footer);color:#cfcfcf}
.foot-col{position:absolute;top:68px;font-size:11.5px;line-height:26px}
.foot-col h5{font-size:12px;font-weight:500;color:var(--white);border-left:2px solid var(--green);padding-left:10px;margin-bottom:8px}
.foot-col span{display:block;padding-left:16px;color:#cfcfcf}
.foot-rule{position:absolute;left:143px;width:914px;height:1px;background:#444}
.foot-nav a{position:absolute;top:199px;font-size:12px;color:var(--white);text-decoration:none}
.social{position:absolute;top:195px;width:18px;height:18px;border:1.5px solid var(--white);border-radius:3px}
.copyright{position:absolute;top:252px;left:0;width:1200px;text-align:center;font-size:10px;color:#8a8a8a}
</style>
</head>
<body>

<header class="site-header">
  <div class="brand"><span class="brand-square"></span><span>Larchmere<br>Hockey Academy</span></div>
  <nav class="nav">
    <a style="left:424px">About us</a>
    <a style="left:510px">Our Programs</a>
    <a style="left:632px">Tournament</a>
    <a style="left:748px">Team</a>
    <a style="left:808px">Contact us</a>
  </nav>
  <div class="btn" style="left:927px;top:24px;width:130px;height:34px">Join us</div>
</header>

<section class="hero">
  <div class="photo" role="img" aria-label="Young hockey player in a red jersey and blue helmet skating with a stick on an indoor rink" style="left:0;top:83px;width:1200px;height:657px;background:linear-gradient(180deg,#0d0d0d 0%,#1e1e1e 45%,#5c5c5c 80%,#b8b8b8 100%)"></div>
  <div class="photo" role="img" aria-label="Hockey player close-up" style="left:640px;top:190px;width:290px;height:520px;background:radial-gradient(ellipse at 50% 45%,#7a2a30 0%,#3a2427 55%,transparent 75%)"></div>
  <h1 class="hero-title display" style="top:298px">Larchmere</h1>
  <h1 class="hero-title display" style="top:355px">Ice Hockey Development</h1>
  <p class="hero-copy">Think you feel too tired to work out? Think again. Your fatigue may be mental rather than physical. Here's how to tell and how to coerce yourself into a training</p>
  <div class="btn" style="left:145px;top:495px;width:175px;height:42px">Our Programs</div>
  <span class="abs" style="left:68px;top:330px;width:14px;height:14px;border:1.5px solid var(--green);border-radius:50%"></span>
  <span class="abs" style="left:72px;top:334px;width:6px;height:6px;border-radius:50%;background:var(--green)"></span>
  <span class="slider-dot" style="top:359px"></span>
  <span class="slider-dot" style="top:382px"></span>
  <span class="abs" style="left:75px;top:402px;width:1px;height:78px;background:#bbb"></span>
  <span class="abs" style="left:68px;top:483px;font-size:10px;color:var(--white)">1/3</span>
</section>

<section class="about">
  <div class="photo" role="img" aria-label="Youth hockey players battling for the puck on an outdoor rink" style="left:0;top:797px;width:543px;height:416px;background:linear-gradient(170deg,#c9ccd1 0%,#8e9197 55%,#d6d8dc 100%)"></div>
  <span class="side-label" style="left:580px;top:838px">About us</span>
  <h2 class="display abs" style="left:613px;top:828px;font-size:36px">Welcome to</h2>
  <h2 class="display abs" style="left:613px;top:883px;font-size:36px">Larchmere Ice Hockey Development</h2>
  <p class="body-copy" style="left:613px;top:948px;width:445px">Li Europan lingues es membres del sam familie. Lor separat existentie es un myth. Por scientie, musica, sport etc, litot Europa usa li sam vocabular. Li lingues differe solmen in li grammatica, li pronunciation e li plu commun vocabules. Omnicos directe al desirabilite de un nov lingua franca: On refusa continuar payar custosi traductores.</p>
  <p class="body-copy" style="left:613px;top:1074px;width:445px">At solmen va esser necessi far uniform grammatica, pronunciation e plu sommun paroles. Ma quande lingues coalesce, li grammatica del resultant lingue es plu simplic e regulari quam ti del coalescent lingues. Li nov lingua franca va esser plu simplic e regulari quam li existent Europan lingues.</p>
</section>

<section class="programs">
  <span class="side-label green" style="left:114px;top:1338px">Our Programs</span>
  <h2 class="display abs" style="left:143px;top:1337px;font-size:36px">We providing the</h2>
  <h2 class="display abs" style="left:143px;top:1393px;font-size:36px">ultimate ice</h2>
  <h2 class="display abs" style="left:143px;top:1449px;font-size:36px">hockey experience ...</h2>

  <div class="dots" style="left:876px;top:1230px;width:210px;height:12px"></div>
  <div class="dots" style="left:1062px;top:1242px;width:12px;height:170px"></div>
  <div class="photo" role="img" aria-label="Children skating and playing hockey on a frozen pond" style="left:615px;top:1260px;width:441px;height:513px;background:linear-gradient(180deg,#d9dbe0 0%,#aeb4bc 50%,#cfd4d9 100%)"></div>
  <div class="prog-num" style="left:617px;top:1800px">1</div>
  <span class="prog-num-label" style="left:622px;top:1858px">program</span>
  <div class="prog-title" style="left:695px;top:1810px">Winter Program</div>
  <p class="prog-desc" style="left:697px;top:1847px">Lorem ipsum dolor sit amet, consectetuer adipiscing elit. Aenean commodo ligula eget dui.</p>

  <div class="dots" style="left:116px;top:1566px;width:210px;height:12px"></div>
  <div class="dots" style="left:116px;top:1578px;width:12px;height:165px"></div>
  <div class="photo" role="img" aria-label="Child in a blue winter jacket holding a hockey stick on outdoor ice" style="left:143px;top:1583px;width:440px;height:494px;background:linear-gradient(180deg,#6b4a2e 0%,#d8e4ec 45%,#c7dbe6 100%)"></div>
  <div class="prog-num" style="left:143px;top:2105px">2</div>
  <span class="prog-num-label" style="left:149px;top:2163px">program</span>
  <div class="prog-title" style="left:222px;top:2113px">Spring Program</div>
  <p class="prog-desc" style="left:223px;top:2153px">Lorem ipsum dolor sit amet, consectetuer adipiscing elit. Aenean commodo ligula eget dui.</p>

  <h2 class="display abs" style="left:143px;top:2330px;font-size:40px;text-transform:none">... enjoy yourfelf</h2>
  <h2 class="display abs" style="left:143px;top:2388px;font-size:40px;text-transform:none">with our programs.</h2>

  <div class="dots" style="left:876px;top:1905px;width:210px;height:12px"></div>
  <div class="dots" style="left:1062px;top:1917px;width:12px;height:165px"></div>
  <div class="photo" role="img" aria-label="Players in red jerseys skating on an outdoor rink at sunset" style="left:617px;top:1933px;width:440px;height:509px;background:linear-gradient(180deg,#bcd3ea 0%,#f0b35a 35%,#8b5a2b 50%,#dfe7ef 70%,#aac6e0 100%)"></div>
  <div class="prog-num" style="left:618px;top:2470px">3</div>
  <span class="prog-num-label" style="left:624px;top:2528px">programs</span>
  <div class="prog-title" style="left:697px;top:2478px">Summer Program</div>
  <p class="prog-desc" style="left:698px;top:2517px">Lorem ipsum dolor sit amet, consectetuer adipiscing elit. Aenean commodo ligula eget dui.</p>
</section>

<section class="tournament">
  <div class="abs" style="left:0;top:2648px;width:1200px;height:570px;background:linear-gradient(90deg,#e4e6e8 0%,#f3f4f5 60%,#eef0f1 100%)"></div>
  <div class="photo" role="img" aria-label="Young hockey player in a red jersey skating on an indoor rink" style="left:150px;top:2570px;width:300px;height:560px;background:radial-gradient(ellipse at 50% 45%,#8a2a30 0%,#4a3a3c 45%,transparent 72%)"></div>
  <span class="side-label" style="left:560px;top:2733px">Tournament</span>
  <h2 class="display abs" style="left:593px;top:2732px;font-size:36px">Ice Hockey</h2>
  <h2 class="display abs" style="left:593px;top:2788px;font-size:36px">Tournament ...</h2>

  <article class="t-card solid" style="left:567px">
    <h3>2023 Larchmere</h3>
    <h4>Ice Hockey Tournament</h4>
    <span class="date">23rd March</span>
    <div class="place">FINLAND &amp; LATVIA, Tampere, Riga</div>
    <p>Lorem ipsum dolor sit amet, consectetuer adipiscing elit. Aenean commodo</p>
    <span class="card-btn">Join us</span>
  </article>
  <article class="t-card outline" style="left:820px">
    <h3 style="color:var(--green)">2023 Larchmere</h3>
    <h4>Ice Hockey Tournament</h4>
    <span class="date">23rd March</span>
    <div class="place">FINLAND &amp; LATVIA, Tampere, Riga</div>
    <p>Lorem ipsum dolor sit amet, consectetuer adipiscing elit. Aenean commodo</p>
    <span class="card-btn">Join us</span>
  </article>
  <svg class="abs" style="left:1035px;top:2985px" width="38" height="38" viewBox="0 0 38 38" aria-hidden="true">
    <circle cx="19" cy="19" r="19" fill="#1f8f1f"/>
    <path d="M16 13l6 6-6 6" fill="none" stroke="#fff" stroke-width="2" stroke-linecap="round" stroke-linejoin="round"/>
  </svg>
</section>

<section class="team">
  <span class="side-label" style="left:450px;top:3273px">Our Team</span>
  <h2 class="display abs" style="left:485px;top:3267px;font-size:36px">Meet our</h2>
  <h2 class="display abs" style="left:485px;top:3323px;font-size:36px">expert instructors</h2>

  <div class="photo" role="img" aria-label="Instructor portrait in a dark hockey jersey holding a stick" style="left:143px;top:3398px;width:292px;height:327px;background:radial-gradient(ellipse at 50% 40%,#5a4a4c 0%,#1a1a1e 70%)"></div>
  <div class="coach-name" style="left:168px;width:242px">Arlo Vennick</div>
  <div class="photo" role="img" aria-label="Instructor portrait in a blue hockey jersey with helmet" style="left:455px;top:3398px;width:290px;height:327px;background:radial-gradient(ellipse at 50% 45%,#2f4f86 0%,#18202e 70%)"></div>
  <div class="coach-name" style="left:480px;width:240px">Ewan Taskett</div>
  <div class="photo" role="img" aria-label="Instructor portrait in a green hockey jersey with white helmet" style="left:766px;top:3398px;width:292px;height:327px;background:radial-gradient(ellipse at 50% 45%,#2d7a4c 0%,#161b19 70%)"></div>
  <div class="coach-name" style="left:791px;width:242px">Rory Halden</div>
</section>

<section class="newsletter">
  <div class="abs" style="left:0;top:3828px;width:1200px;height:242px;background:linear-gradient(90deg,#e6e7e9 0%,#eeeff0 100%)"></div>
  <div class="photo" role="img" aria-label="Overhead view of two hockey players skating on white ice" style="left:660px;top:3828px;width:540px;height:242px;background:radial-gradient(ellipse at 40% 40%,#b8bcc0 0%,transparent 55%),radial-gradient(ellipse at 80% 55%,#a9adb1 0%,transparent 50%)"></div>
  <h2 class="display abs" style="left:140px;top:3868px;font-size:27px;text-transform:none">Subscribe To Our Newsletter</h2>
  <p class="abs" style="left:141px;top:3918px;font-size:9.5px;color:var(--ink)">Subscribe to our mailing list for news, updates and exclusive offers!</p>
  <div class="news-input">Enter Your Email Address</div>
  <svg class="abs" style="left:158px;top:3977px" width="16" height="12" viewBox="0 0 16 12" aria-hidden="true">
    <rect x="0.75" y="0.75" width="14.5" height="10.5" fill="none" stroke="#555" stroke-width="1.3"/>
    <path d="M1 1l7 6 7-6" fill="none" stroke="#555" stroke-width="1.3"/>
  </svg>
  <div class="news-btn">Subscribe</div>
</section>

<footer class="site-footer">
  <div class="brand" style="left:143px;top:62px;color:var(--white);font-size:26px;gap:12px"><span class="brand-square" style="width:20px;height:20px"></span><span>Larchmere<br>Hockey Academy</span></div>
  <div class="foot-col" style="left:427px">
    <h5>Address</h5>
    <span>14 Fenwick Lane, Corbridge,</span>
    <span>NT 20418</span>
  </div>
  <div class="foot-col" style="left:686px">
    <h5>Contact us</h5>
    <span>1-555-010-2841</span>
    <span>contact@larchmerehockey.com</span>
  </div>
  <div class="foot-col" style="left:918px">
    <h5>Program hours</h5>
    <span>Mon – Fri: 9.00 – 6.00</span>
    <span>Sat – Sun: 9.00 – 1.00</span>
  </div>
  <div class="foot-rule" style="top:175px"></div>
  <nav class="foot-nav">
    <a style="left:147px">Home</a>
    <a style="left:218px">About us</a>
    <a style="left:315px">Programs</a>
    <a style="left:415px">Tournament</a>
    <a style="left:526px">Contact us</a>
    <a style="left:645px">Members Login</a>
    <a style="left:786px">Our Team</a>
  </nav>
  <span class="social" style="left:928px"></span>
  <span class="social" style="left:977px"></span>
  <span class="social" style="left:1030px"></span>
  <div class="foot-rule" style="top:235px"></div>
  <p class="copyright">©Copyright 2023 Larchmere Hockey Academy. All Rights Reserved</p>
</footer>

</body>
</html>
```